Manual design

Hello,

I am looking for someone creative to help me design my Real Estate related manual. I am looking for something simple yet impressive. It would be designed around my logo and brand colors and I would also like it to have a local feel, perhaps with photos I could provide of my area/hometown. I am really shooting for an impressive company and branded look, while keeping it neat without too much going on.

I have the content that I would like to include, I am just struggling with the design of the manual in general.

I have attached a copy of my logo, my companys logo, and a publisher file of what I had previously done. Please do not think the design I previously used is something to work off of if you deem it better to use another feel. I am looking for originality, unless you can improve upon my old file. Any questions, please feel free to reach out to me.

The content in the provided brochure will remain the same, it is the design aspect I need help with. Thanks

Target Market(s)

My target market is home sellers aged 25-55, people usually selling their 1st or second home

Industry/Entity Type

Real Estate

Requirements
Must have
• -A simple to read design focused around my logo and colors
-A local sense
Should not have
• Drawings, only real photos

```html
<!DOCTYPE html>
<html lang="en">
<head>
<meta charset="utf-8">
<title>Marketing Systems Cont.</title>
<link rel="stylesheet" href="https://fonts.googleapis.com/css2?family=Arimo:wght@400;700&display=swap">
<style>
  :root {
    --brand-blue: #0d5fae;
    --brand-blue-dark: #0a4f93;
    --gold: #ddaa0c;
    --heading-grey: #555555;
    --panel-bg: #f7f7f7;
    --panel-border: #c9c9c9;
    --title-bg: #f4f4f4;
    --title-border: #dcdcdc;
    --ink: #111111;
    --white: #ffffff;
    --logo-slate: #5a6a8e;
    --logo-navy: #2a3f6e;
  }
  * { box-sizing: border-box; margin: 0; padding: 0; }
  html, body { width: 1200px; height: 900px; overflow: hidden; background: var(--white); }
  body { font-family: "Arimo", Arial, sans-serif; position: relative; }

  .sidebar {
    position: absolute; left: 0; top: 0; width: 150px; height: 900px;
    background: linear-gradient(180deg, var(--brand-blue) 0%, var(--brand-blue-dark) 100%);
    color: var(--white);
  }
  .sidebar__quote {
    position: absolute; left: 75px; top: 390px;
    transform: translate(-50%, -50%) rotate(-90deg);
    width: 700px; text-align: center;
    font-weight: 700; font-size: 23px; line-height: 29px;
  }
  .sidebar__contact {
    position: absolute; left: 20px; top: 790px;
    font-weight: 700; font-size: 12px; line-height: 15px;
  }
  .sidebar__name { font-size: 14px; line-height: 17px; }
  .sidebar__email { margin-top: 15px; }

  .page-title {
    position: absolute; left: 170px; top: 14px; width: 666px; height: 94px;
    background: var(--title-bg); border: 1px solid var(--title-border);
    display: flex; align-items: center; padding-left: 25px;
    color: var(--gold); font-weight: 700; font-size: 41.5px; letter-spacing: 0.5px;
  }

  .brand {
    position: absolute; top: 18px; height: 84px;
    display: flex; flex-direction: column; align-items: center; justify-content: center; gap: 6px;
    font-weight: 700; text-align: center;
  }
  .brand--agent { left: 890px; width: 112px; color: var(--logo-slate); font-size: 16px; }
  .brand--agent .brand__mark { width: 18px; height: 18px; background: var(--logo-slate); }
  .brand--office { left: 1018px; width: 144px; color: var(--logo-navy); font-size: 20px; line-height: 22px; gap: 0; }

  .skyline {
    position: absolute; left: 270px; top: 700px; width: 900px; height: 200px;
    background: linear-gradient(180deg, rgba(255,255,255,0) 0%, rgba(200,200,200,0.35) 100%);
  }

  .content {
    position: absolute; left: 168px; top: 124px; width: 993px; height: 677px;
    background: var(--panel-bg); border: 2px solid var(--panel-border);
    padding: 22px 0 0 34px;
  }
  .section-heading {
    display: inline-block; color: var(--heading-grey);
    font-weight: 700; font-size: 31px; line-height: 36px;
    border-bottom: 3px solid var(--gold); padding-right: 6px;
  }
  .point-list { list-style: none; margin: 30px 0 0 40px; }
  .point-list + .section-heading { margin-top: 28px; }
  .point {
    position: relative; padding-left: 35px; width: 760px;
    font-weight: 700; font-size: 16px; line-height: 19.5px; color: var(--ink);
  }
  .point + .point { margin-top: 33px; }
  .point__arrow { position: absolute; left: 0; top: 2px; width: 22px; height: 16px; }

  .page-number {
    position: absolute; right: 14px; bottom: 12px;
    font-weight: 700; font-size: 22px; color: var(--ink);
  }
</style>
</head>
<body>
  <aside class="sidebar">
    <p class="sidebar__quote">“By failing to to prepare, you are preparing to fail”<br>-Elias Thorne</p>
    <div class="sidebar__contact">
      <p class="sidebar__name">Carlen Ashby</p>
      <p>Multi-Award Winning<br>Estate Professional<br>555-210-4487</p>
      <p class="sidebar__email">homes@ashby.ca</p>
    </div>
  </aside>

  <h1 class="page-title">MARKETING SYSTEMS CONT.</h1>

  <div class="brand brand--agent"><span class="brand__mark"></span><span>ashby.ca</span></div>
  <div class="brand brand--office"><span>Northgate</span><span>Realty</span></div>

  <div class="skyline" role="img" aria-label="Outline of the local city skyline with towers and rooftops"></div>

  <main class="content">
    <h2 class="section-heading">Real State Community cont...</h2>
    <ul class="point-list">
      <li class="point">
        <svg class="point__arrow" viewBox="0 0 22 16"><path d="M1 5h11V1l9 7-9 7v-4H1z" fill="#000"/></svg>
        Lorem ipsum dolor sit amet, consectetur adipiscing elit. Donec id massa porta magna varius molestie. Sed nisl neque, consequat vitae vestibulum non, interdum sit amet augue. Cras quis nibh est. Aliquam est nisi, rutrum vitae ultrices sed, blandit et neque. Aliquam pretium, tortor facilisis luctus varius, sapien felis malesuada eros, sed pharetra libero nisl sit amet lorem. Pellentesque vitae pulvinar dui.
      </li>
      <li class="point">
        <svg class="point__arrow" viewBox="0 0 22 16"><path d="M1 5h11V1l9 7-9 7v-4H1z" fill="#000"/></svg>
        Lorem ipsum dolor sit amet, consectetur adipiscing elit. Donec id massa porta magna varius molestie. Sed nisl neque, consequat vitae vestibulum non, interdum sit amet augue. Cras quis nibh est. Aliquam est nisi, rutrum vitae ultrices sed, blandit et neque. Aliquam pretium, tortor facilisis luctus varius, sapien felis malesuada eros, sed pharetra libero nisl sit amet lorem. Pellentesque vitae pulvinar dui.
      </li>
    </ul>

    <h2 class="section-heading">Lawn&nbsp; Sign/Open House</h2>
    <ul class="point-list">
      <li class="point">
        <svg class="point__arrow" viewBox="0 0 22 16"><path d="M1 5h11V1l9 7-9 7v-4H1z" fill="#000"/></svg>
        Lorem ipsum dolor sit amet, consectetur adipiscing elit. Donec id massa porta magna varius molestie. Sed nisl neque, consequat vitae vestibulum non, interdum sit amet augue. Cras quis nibh est. Aliquam est nisi, rutrum vitae ultrices sed, blandit et neque. Aliquam pretium, tortor facilisis luctus varius, sapien felis malesuada eros, sed pharetra libero nisl sit amet lorem. Pellentesque vitae pulvinar dui.
      </li>
    </ul>
  </main>

  <span class="page-number">7</span>
</body>
</html>
```